Bright Harbor Counseling Letterhead for hip modern business

I would like some ombre use of the colors in the logo hip letterhead that incorporates logo colors and feel, needs to connect with young professionals and college students. i need to be able to write letters to schools to excuse absences as well. i like color blocks on one side preferably using colors from the attached logo design.

Target Market(s)

high income young people, young adults and college students

Industry/Entity Type

mental health

Font styles to use
Serif
Sans Serif

Colors
0054AA
0677BA
7BADD7
CADEEF
E8F1F8
0094D4
00A9DD
6FCCEA
C7EBF8
E9F6FB
00AB8E
00BBA5
67D7C9
C6EFE9
E9F9F6
59FF00
82FF00
B8FF75
E3FFCB
F4FFEA
A7469A
B969AE
D3A5CF
EDDBEB
F8F0F9
6B429C
8869AF
B7A5CE
E3DAEB
F3F0F8

Requirements
Must have
• a modern hip feel, somewhat color

```html
<!DOCTYPE html>
<html lang="en">
<head>
<meta charset="utf-8">
<title>Bright Harbor Counseling – Stationery</title>
<link href="https://fonts.googleapis.com/css2?family=Nunito+Sans:wght@300;400&family=Open+Sans:wght@400;600&display=swap" rel="stylesheet">
<style>
  :root{
    --bg:#e9e9eb;
    --paper:#ffffff;
    --ink:#4a4a4f;
    --purple:#7b3b80;
    --blue:#2a6fb0;
    --accent:#8869af;
    --rule:#dcdce0;
  }
  *{box-sizing:border-box;margin:0;padding:0}
  html,body{width:1200px;height:795px;overflow:hidden;background:var(--bg)}
  body{position:relative;font-family:"Open Sans",sans-serif;color:var(--ink)}

  .letterhead{
    position:absolute;left:80px;top:60px;width:520px;height:673px;
    background:var(--paper);box-shadow:0 10px 30px rgba(0,0,0,.12);
    overflow:hidden;
  }
  .brand{
    position:absolute;right:48px;top:40px;display:flex;align-items:center;gap:10px;
    font-family:"Nunito Sans",sans-serif;font-weight:300;color:var(--ink);
  }
  .brand-name{font-size:22px;line-height:1.05;text-align:right}
  .brand-name small{display:block;font-size:11px;letter-spacing:3px}
  .brand-dot{width:34px;height:34px;border-radius:50%;background:var(--accent)}

  .contact{
    position:absolute;right:48px;top:106px;font-size:9px;line-height:1.65;color:var(--ink);
  }
  .contact li{list-style:none;display:flex;justify-content:flex-end;align-items:center;gap:5px}
  .contact svg{width:9px;height:9px;fill:var(--blue);flex:none}

  .letter-body{
    position:absolute;left:48px;top:200px;width:424px;font-size:9px;line-height:1.5;color:var(--ink);
  }
  .letter-body p{margin-bottom:9px}
  .salutation{margin-bottom:8px}
  .signoff{margin-top:14px;margin-bottom:6px}
  .signature{display:block;width:80px;height:36px;background:linear-gradient(90deg,#e6e6ea,#f4f4f6);border-radius:3px}

  .footer-rule{position:absolute;left:0;bottom:30px;width:330px;height:9px;background:var(--purple)}
  .footer-band{
    position:absolute;right:0;bottom:0;width:220px;height:32px;background:var(--blue);
    clip-path:polygon(12px 0,100% 0,100% 100%,0 100%);
    color:#fff;font-size:12px;font-weight:600;display:flex;align-items:center;justify-content:center;letter-spacing:.3px;
  }

  .envelope{
    position:absolute;left:640px;top:300px;width:500px;height:230px;
    background:var(--paper);box-shadow:0 10px 30px rgba(0,0,0,.12);
  }
  .envelope .brand{right:36px;top:32px}
  .envelope .brand-name{font-size:19px}
  .envelope .brand-name small{font-size:10px}
  .envelope .brand-dot{width:28px;height:28px}
  .envelope-window{position:absolute;left:36px;top:110px;width:210px;height:70px;border:1px solid var(--rule);border-radius:4px}
</style>
</head>
<body>
  <article class="letterhead">
    <header class="brand">
      <div class="brand-name">Bright Harbor<small>Counseling</small></div>
      <span class="brand-dot"></span>
    </header>

    <ul class="contact">
      <li>48 Linden Court Road,</li>
      <li>Maple Grove, ON L5T 3K2</li>
      <li><svg viewBox="0 0 10 10"><path d="M2 0h2l1 3-1.5 1a6 6 0 0 0 2.5 2.5L7 5l3 1v2a2 2 0 0 1-2 2A8 8 0 0 1 0 2a2 2 0 0 1 2-2z"/></svg>(555) 204-3170</li>
      <li><svg viewBox="0 0 10 10"><rect x="1" y="3" width="8" height="6" rx="1"/><rect x="3" y="0" width="4" height="3"/></svg>(555) 318-6642</li>
      <li><svg viewBox="0 0 10 10"><rect x="0" y="2" width="10" height="7" rx="1"/></svg>hello@brightharbor.com</li>
    </ul>

    <section class="letter-body">
      <p class="salutation">Dear customer,</p>
      <p>Lorem ipsum dolor sit amet, consectetur adipisicing elit, sed do eiusmod tempor incididunt ut labore et dolore magna aliqua. Ut enim ad minim veniam, quis nostrud exercitation ullamco laboris nisi ut aliquip ex ea commodo consequat. Duis aute irure dolor in reprehenderit in voluptate velit esse cillum dolore eu fugiat nulla pariatur. Excepteur sint occaecat cupidatat non proident, sunt in culpa qui officia deserunt mollit anim id est laborum.</p>
      <p>Lorem ipsum dolor sit amet, consectetur adipisicing elit, sed do eiusmod tempor incididunt ut labore et dolore magna aliqua. Ut enim ad minim veniam, quis nostrud exercitation ullamco laboris nisi ut aliquip ex ea commodo consequat. Duis aute irure dolor in reprehenderit in voluptate velit esse cillum dolore eu fugiat nulla pariatur. Excepteur sint occaecat cupidatat non proident, sunt in culpa qui officia deserunt mollit anim id est laborum.</p>
      <p>Lorem ipsum dolor sit amet, consectetur adipisicing elit, sed do eiusmod tempor incididunt ut labore et dolore magna aliqua. Ut enim ad minim veniam, quis nostrud exercitation ullamco laboris nisi ut aliquip ex ea commodo consequat. Duis aute irure dolor in reprehenderit in voluptate velit esse cillum dolore eu fugiat nulla pariatur. Excepteur sint occaecat cupidatat non proident, sunt in culpa qui officia deserunt mollit anim id est laborum.</p>
      <p>Lorem ipsum dolor sit amet, consectetur adipisicing elit, sed do eiusmod tempor incididunt ut labore et dolore magna aliqua. Ut enim ad minim veniam, quis nostrud exercitation ullamco laboris nisi ut aliquip ex ea commodo consequat. Duis aute irure dolor.</p>
      <p class="signoff">Yours Sincerely,</p>
      <span class="signature" role="img" aria-label="Handwritten signature"></span>
    </section>

    <div class="footer-rule"></div>
    <div class="footer-band">www.brightharbor.com</div>
  </article>

  <article class="envelope">
    <header class="brand">
      <div class="brand-name">Bright Harbor<small>Counseling</small></div>
      <span class="brand-dot"></span>
    </header>
    <div class="envelope-window"></div>
  </article>
</body>
</html>
```